Real Estate Company Needs Business Card Designed

We need a business card design for a new real estate company based in Campbell, CA (Silicon Valley). We plan to improve the residential real estate industry by using technology to improve customer experience. We would like to see designs that use a black background. The final design should communicate sophistication and customer service, as well as stability and technology.

Industry/Entity Type

Real Estate

Requirements
Must have
• Black background

```html
<!DOCTYPE html>
<html lang="en">
<head>
<meta charset="utf-8">
<title>Velmont Real Estate Services – Business Card</title>
<link href="https://fonts.googleapis.com/css2?family=Montserrat:wght@900&family=Syncopate:wght@400;700&display=swap" rel="stylesheet">
<style>
  :root {
    --card-black: #121519;
    --swoosh-dark: #1b1f25;
    --swoosh-mid: #171a1f;
    --accent-blue: #2f78e0;
    --text-white: #f4f6f9;
    --tagline-grey: #8c9bb4;
  }
  html, body {
    margin: 0;
    padding: 0;
    width: 1200px;
    height: 686px;
    overflow: hidden;
    background: var(--card-black);
  }
  .card {
    position: relative;
    width: 1200px;
    height: 686px;
    background: var(--card-black);
    overflow: hidden;
    font-family: "Syncopate", "Arial", sans-serif;
    color: var(--text-white);
  }
  .card-backdrop {
    position: absolute;
    inset: 0;
  }
  .divider {
    position: absolute;
    left: 611px;
    top: 67px;
    width: 3px;
    height: 552px;
    background: var(--accent-blue);
  }
  .identity {
    position: absolute;
    right: 646px;
    top: 172px;
    text-align: right;
  }
  .person-name {
    margin: 0;
    font-family: "Montserrat", "Arial Black", sans-serif;
    font-weight: 900;
    font-size: 56px;
    line-height: 1;
    letter-spacing: 1px;
    color: var(--text-white);
  }
  .person-title {
    margin: 14px 0 0;
    font-size: 23px;
    font-weight: 400;
    text-transform: lowercase;
    color: var(--accent-blue);
    letter-spacing: 1px;
  }
  .brand-block {
    position: absolute;
    left: 66px;
    top: 440px;
    width: 470px;
    text-align: center;
  }
  .brand-name {
    font-size: 62px;
    font-weight: 400;
    line-height: 1;
    color: var(--text-white);
    letter-spacing: 2px;
  }
  .brand-tagline {
    margin-top: 22px;
    font-size: 19px;
    font-weight: 400;
    color: var(--tagline-grey);
    letter-spacing: 4px;
  }
  .brand-mark {
    position: absolute;
    left: 760px;
    top: 150px;
    width: 256px;
    text-align: center;
    font-size: 40px;
    font-weight: 400;
    letter-spacing: 2px;
    color: var(--text-white);
  }
  .contact {
    position: absolute;
    right: 43px;
    text-align: right;
    font-size: 24px;
    font-weight: 400;
    text-transform: lowercase;
    line-height: 41px;
    letter-spacing: 1px;
    margin: 0;
    font-style: normal;
  }
  .contact-address { top: 342px; }
  .contact-digital { top: 481px; }
  .contact-line { display: block; white-space: nowrap; }
  .is-accent { color: var(--accent-blue); }
</style>
</head>
<body>
  <main class="card">
    <svg class="card-backdrop" width="1200" height="686" viewBox="0 0 1200 686" aria-hidden="true">
      <path d="M0 0 H560 C420 60 250 170 0 330 Z" fill="var(--swoosh-mid)"/>
      <path d="M0 0 H330 C230 50 120 120 0 200 Z" fill="var(--swoosh-dark)"/>
      <path d="M640 0 H1200 V40 C1000 20 820 30 640 0 Z" fill="var(--swoosh-mid)"/>
    </svg>

    <div class="divider"></div>

    <section class="identity">
      <h1 class="person-name">DANIEL REYES</h1>
      <p class="person-title">Vice President</p>
    </section>

    <section class="brand-block">
      <div class="brand-name">VELMONT</div>
      <div class="brand-tagline">REAL ESTATE SERVICES</div>
    </section>

    <div class="brand-mark">VELMONT</div>

    <address class="contact contact-address">
      <span class="contact-line">2450 Orchard Park Blvd.,</span>
      <span class="contact-line">6th Floor, Campbell</span>
      <span class="contact-line is-accent">95008</span>
    </address>

    <address class="contact contact-digital">
      <span class="contact-line">danielreyes<span class="is-accent">@</span>velmont.com</span>
      <span class="contact-line is-accent">+1 (408) 555-0187</span>
      <span class="contact-line is-accent">www.velmont.com</span>
    </address>
  </main>
</body>
</html>
```